Create a professional, eye-catching business card design that reflects the values and services of Brookfern Veterinary Hospital. we provide veterinary services and the business card should be a memorable representation of the clinic and align with its branding and mission. our tag line is "Life Long Companions, Lifelong Care"
Use clean, modern typography. Prioritize readability and professionalism. We would like to see designs that use the color blue, as in the logo example. the final design should communicate professionalism and care, with attention to detail.

```html
<!DOCTYPE html>
<html lang="en">
<head>
<meta charset="utf-8">
<title>Brookfern Veterinary Hospital – Business Card</title>
<link href="https://fonts.googleapis.com/css2?family=Poppins:wght@400;600&family=Patrick+Hand&display=swap" rel="stylesheet">
<style>
  :root {
    --stage: #5c5c5c;
    --blue-light: #3a73ee;
    --blue-deep: #1d44ad;
    --yellow: #fed700;
    --wave-edge: #5cb8f5;
    --navy: #1f3a86;
    --ink: #1b1b24;
    --white: #ffffff;
  }
  * { margin: 0; padding: 0; box-sizing: border-box; }
  html, body { width: 1200px; height: 1052px; overflow: hidden; }
  body { background: var(--stage); position: relative; font-family: "Poppins", sans-serif; }

  .card {
    position: absolute; top: 135px; width: 448px; height: 784px; overflow: hidden;
    background: radial-gradient(ellipse at 50% 45%, var(--blue-light) 0%, #2d5fd9 45%, var(--blue-deep) 100%);
    box-shadow: 0 8px 18px rgba(0,0,0,.35);
  }
  .card--front { left: 152px; }
  .card--back { left: 632px; }

  .brand { position: absolute; top: 56px; left: 0; width: 100%; text-align: center; color: var(--white); font-weight: 600; }
  .brand__ring { width: 110px; height: 110px; margin: 0 auto 14px; border: 2px solid var(--white); border-radius: 50%; }
  .brand__name { font-size: 33px; line-height: 1; letter-spacing: 1px; }
  .brand__sub { font-size: 11.5px; letter-spacing: 1.3px; margin-top: 3px; }

  .wave { position: absolute; inset: 0; width: 100%; height: 100%; }

  .pets-photo {
    position: absolute; left: 58px; top: 258px; width: 390px; height: 322px;
    background: radial-gradient(ellipse at 50% 55%, #d9b27e 0%, #c79a62 40%, rgba(160,140,120,.6) 70%, rgba(58,115,238,0) 90%);
  }

  .tagline {
    position: absolute; top: 630px; left: 0; width: 100%; text-align: center;
    font-family: "Patrick Hand", cursive; color: var(--navy); font-size: 42px; line-height: 42px;
  }

  .person { position: absolute; top: 258px; left: 0; width: 100%; text-align: center; }
  .person__name { font-family: "Patrick Hand", cursive; color: var(--yellow); font-size: 48px; line-height: 52px; }
  .person__role { color: var(--white); font-size: 20px; line-height: 24px; }

  .contact-icons { position: absolute; top: 458px; left: 0; width: 100%; display: flex; justify-content: center; gap: 17px; }
  .contact-icons svg { width: 34px; height: 34px; }

  .contact { position: absolute; top: 515px; left: 0; width: 100%; text-align: center; color: var(--ink); font-size: 20px; }
  .contact__address { line-height: 26px; }
  .contact__phone { margin-top: 16px; }
  .contact__email { margin-top: 16px; }
  .contact__web { margin-top: 16px; }
</style>
</head>
<body>

<section class="card card--front">
  <div class="brand">
    <div class="brand__ring"></div>
    <div class="brand__name">BROOKFERN</div>
    <div class="brand__sub">VETERINARY HOSPITAL</div>
  </div>

  <div class="pets-photo" role="img" aria-label="Photo of a golden labrador, a grey rabbit and a ginger kitten sitting together"></div>

  <svg class="wave" viewBox="0 0 448 784" preserveAspectRatio="none" aria-hidden="true">
    <path d="M0 560 C30 548 55 576 88 577 C115 578 128 560 150 560 C185 560 200 582 232 581 C270 580 310 548 358 547 C395 546 420 568 448 570" fill="none" stroke="var(--wave-edge)" stroke-width="6"/>
    <path d="M0 566 C30 554 55 582 88 583 C115 584 128 566 150 566 C185 566 200 588 232 587 C270 586 310 554 358 553 C395 552 420 574 448 576 L448 784 L0 784 Z" fill="var(--yellow)"/>
  </svg>

  <p class="tagline">Life Long Companions,<br>Lifelong Care..</p>
</section>

<section class="card card--back">
  <div class="brand">
    <div class="brand__ring"></div>
    <div class="brand__name">BROOKFERN</div>
    <div class="brand__sub">VETERINARY HOSPITAL</div>
  </div>

  <div class="person">
    <div class="person__name">Maisie Carrington</div>
    <div class="person__role">Owner</div>
  </div>

  <svg class="wave" viewBox="0 0 448 784" preserveAspectRatio="none" aria-hidden="true">
    <path d="M0 370 C30 356 55 386 82 387 C110 388 125 368 148 368 C185 368 200 393 232 392 C270 391 295 362 328 362 C370 362 410 374 448 376" fill="none" stroke="var(--wave-edge)" stroke-width="6"/>
    <path d="M0 377 C30 363 55 393 82 394 C110 395 125 375 148 375 C185 375 200 400 232 399 C270 398 295 369 328 369 C370 369 410 381 448 383 L448 784 L0 784 Z" fill="var(--yellow)"/>
  </svg>

  <div class="contact-icons">
    <svg viewBox="0 0 34 34" aria-label="Address"><circle cx="17" cy="17" r="17" fill="var(--navy)"/><path d="M17 8a6 6 0 0 0-6 6c0 4.5 6 11 6 11s6-6.5 6-11a6 6 0 0 0-6-6z" fill="#4a8cf0"/><circle cx="17" cy="14" r="2.2" fill="var(--navy)"/></svg>
    <svg viewBox="0 0 34 34" aria-label="Phone"><circle cx="17" cy="17" r="17" fill="var(--navy)"/><path d="M12 9l3 4-2 2c1 2.5 3 4.5 5.5 5.5l2-2 4 3-1.5 2.5c-6 0-12.5-6.5-12.5-12.5z" fill="#4a8cf0"/></svg>
    <svg viewBox="0 0 34 34" aria-label="Email"><circle cx="17" cy="17" r="17" fill="var(--navy)"/><rect x="9" y="11" width="16" height="12" rx="1.5" fill="#4a8cf0"/><path d="M9.5 12l7.5 6 7.5-6" fill="none" stroke="var(--navy)" stroke-width="1.5"/></svg>
    <svg viewBox="0 0 34 34" aria-label="Website"><circle cx="17" cy="17" r="17" fill="var(--navy)"/><g fill="none" stroke="#4a8cf0" stroke-width="1.6"><circle cx="17" cy="17" r="8"/><ellipse cx="17" cy="17" rx="3.5" ry="8"/><path d="M9 17h16M10.5 13h13M10.5 21h13"/></g></svg>
  </div>

  <div class="contact">
    <p class="contact__address">12 Wattle Road,<br>Glenmere, WA 6081</p>
    <p class="contact__phone">(08) 9400 2871</p>
    <p class="contact__email">reception@brookfernvet.com.au</p>
    <p class="contact__web">www.brookfernvet.com.au</p>
  </div>
</section>

</body>
</html>
```